Corporate Branding - Web and Print

A UK based company will like to use an existing logo to create branding materials for all marketing related documents, including business card, prints, letterhead, Website, Twitter, Facebook, Instagram logo etc. This company serves high-end clientele in the fashion, health and wellness and as such high quality and class is of utmost importance.
Where the logo can be modernised without losing its character then experiment. The main thing is to have a corporate branding which can be used later for brochures, Business Plan infographics.
The prominent colour within the organisation is burnt orange with no secondary colour. However if you believe a secondary colour is needed then use it, otherwise keep it simple and classy. Any chosen colours have to match perfectly.
Target Market(s)
High net worth individuals
Industry/Entity Type
Health And Wellness
Contact Information for Business Card
classy
Look and feel
Each slider illustrates characteristics of the customer's brand and the style your logo design should communicate.

```html
<!DOCTYPE html>
<html lang="en">
<head>
<meta charset="UTF-8">
<title>Velora – Business Card</title>
<link href="https://fonts.googleapis.com/css2?family=Merriweather:wght@400;700&display=swap" rel="stylesheet">
<style>
  :root {
    --burnt-orange: #f39323;
    --card-black: #1b1b1b;
    --card-black-soft: #262626;
    --card-white: #f4f5f6;
    --ink: #1e1e1e;
    --backdrop: #e8e8e9;
  }
  * { box-sizing: border-box; margin: 0; padding: 0; }
  html, body {
    width: 1200px; height: 900px; overflow: hidden;
    background: var(--backdrop);
    font-family: "Merriweather", Georgia, serif;
  }
  .card-set {
    width: 1200px; height: 900px;
    display: flex; align-items: center; justify-content: center; gap: 60px;
  }
  .card {
    width: 500px; height: 286px; border-radius: 16px;
    position: relative; overflow: hidden;
    box-shadow: 0 10px 24px rgba(0,0,0,0.12);
  }
  /* Back of card */
  .card-back {
    background: var(--card-black);
    display: flex; align-items: center; justify-content: center;
  }
  .card-back .pattern-field {
    position: absolute; inset: 0;
    background: linear-gradient(135deg, var(--card-black-soft), var(--card-black));
  }
  .brand-name {
    position: relative;
    color: var(--burnt-orange);
    font-weight: 700;
    font-size: 44px;
    letter-spacing: 4px;
  }
  /* Front of card */
  .card-front {
    background: var(--card-white);
    display: flex; align-items: center;
    padding: 0 34px 0 30px;
  }
  .front-brand {
    flex: 0 0 210px;
    color: var(--burnt-orange);
    font-weight: 700;
    font-size: 38px;
    letter-spacing: 2px;
  }
  .contact-block { flex: 1; }
  .person-name {
    color: var(--burnt-orange);
    font-weight: 700; font-size: 15px; letter-spacing: 0.5px;
  }
  .person-role {
    color: var(--ink); font-size: 14px; margin: 4px 0 12px;
  }
  .contact-list { list-style: none; }
  .contact-list li {
    display: flex; align-items: center; gap: 9px;
    color: var(--ink); font-size: 11px; line-height: 1; margin-bottom: 8px;
  }
  .contact-list svg { width: 12px; height: 12px; flex: 0 0 12px; }
</style>
</head>
<body>
  <main class="card-set">
    <section class="card card-back">
      <div class="pattern-field" role="img" aria-label="Subtle repeating brand pattern on black"></div>
      <div class="brand-name">VELORA</div>
    </section>

    <section class="card card-front">
      <div class="front-brand">VELORA</div>
      <div class="contact-block">
        <div class="person-name">MARCUS HALE</div>
        <div class="person-role">Manager</div>
        <ul class="contact-list">
          <li>
            <svg viewBox="0 0 12 12" aria-hidden="true"><rect x="2.5" y="0.8" width="7" height="10.4" rx="1.2" fill="none" stroke="var(--burnt-orange)" stroke-width="1.3"/><line x1="5" y1="9.3" x2="7" y2="9.3" stroke="var(--burnt-orange)" stroke-width="1"/></svg>
            020-555-0134
          </li>
          <li>
            <svg viewBox="0 0 12 12" aria-hidden="true"><rect x="0.5" y="2.5" width="11" height="7.5" fill="var(--burnt-orange)"/><polyline points="0.8,2.8 6,7 11.2,2.8" fill="none" stroke="var(--card-white)" stroke-width="1"/></svg>
            hello@veloraclinic.com
          </li>
          <li>
            <svg viewBox="0 0 12 12" aria-hidden="true"><circle cx="6" cy="6" r="5.5" fill="var(--burnt-orange)"/><ellipse cx="6" cy="6" rx="2.3" ry="5.3" fill="none" stroke="var(--card-white)" stroke-width="0.8"/><line x1="0.6" y1="6" x2="11.4" y2="6" stroke="var(--card-white)" stroke-width="0.8"/></svg>
            www.veloraclinic.com
          </li>
        </ul>
      </div>
    </section>
  </main>
</body>
</html>
```